Yogurt website Home page

I am looking for some website design/graphics concepts on yogurt shop.

Provide great concept and ideas .
I have attached logo here . we need theme based on our logo .

Let me know if have any question .

=====
geeks , really appreciate who ever maid entry .
i need Home page not only logo.
4 entries which i got so far are on only LOGO .
Am i missing something here ?

```html
<!DOCTYPE html>
<html lang="en">
<head>
<meta charset="utf-8">
<title>Cloudberry Frozen Yogurt – Home</title>
<link href="https://fonts.googleapis.com/css2?family=Open+Sans:wght@400;600;700&family=Days+One&family=Lobster+Two:ital,wght@1,700&display=swap" rel="stylesheet">
<style>
:root{
  --magenta:#c8167e;
  --magenta-dark:#a8106a;
  --purple:#6a1f86;
  --purple-deep:#4b1470;
  --cyan:#1fb6e0;
  --cyan-light:#45d0f2;
  --white:#ffffff;
  --footer:#b5126f;
  --footer-bar:#27b9e2;
}
*{box-sizing:border-box;margin:0;padding:0}
html,body{width:989px;height:1200px;overflow:hidden}
body{font-family:'Open Sans',sans-serif;background:var(--white)}
.page{position:relative;width:989px;height:1200px;overflow:hidden;
  background:linear-gradient(180deg,#d7def2 0%,#e9ecf8 30%,#f6f4fb 55%,#ffffff 75%)}
.abs{position:absolute}
.placeholder{position:absolute}

/* header */
.header{left:0;top:0;width:989px;height:114px;background:linear-gradient(180deg,#cfd7f0,#e4e8f7);border-bottom:3px solid var(--purple-deep)}
.brand-box{left:141px;top:4px;width:164px;height:103px;background:var(--white);box-shadow:0 2px 6px rgba(0,0,0,.25);display:flex;align-items:center;justify-content:center;gap:6px}
.brand-box .dot{width:14px;height:14px;border-radius:50%;background:var(--magenta)}
.brand-box span{font-weight:700;font-size:17px;color:var(--purple)}
.brand-name{left:314px;top:56px;font-weight:700;font-size:24px;line-height:26px;color:var(--purple);white-space:nowrap;z-index:2}
.brand-sub{left:358px;top:88px;font-weight:600;font-size:14px;letter-spacing:1px;color:var(--magenta);white-space:nowrap;z-index:2}
.social-bubble{left:662px;top:24px;width:184px;height:54px;border-radius:27px;background:var(--white);border:2px solid #e0506a;display:flex;align-items:center;justify-content:center;gap:12px}
.social-bubble i{width:34px;height:34px;border-radius:50%;display:block}

/* nav */
.nav{left:0;top:117px;width:989px;height:30px}
.nav a{position:absolute;top:5px;font-family:'Days One',sans-serif;font-size:13.5px;color:var(--purple);text-decoration:none;letter-spacing:.3px;white-space:nowrap}
.nav a.active{background:var(--magenta);color:var(--white);padding:5px 12px 7px;border-radius:14px 14px 0 0;top:0}
.dropdown{left:219px;top:160px;width:106px;height:85px;background:var(--magenta);border-radius:0 0 6px 6px;padding:6px 9px;z-index:3}
.dropdown a{display:block;font-family:'Days One',sans-serif;font-size:10.5px;color:var(--white);text-decoration:none;line-height:18.5px;white-space:nowrap}

/* hero */
.hero{left:134px;top:172px;width:720px;height:302px;border-radius:60px;background:linear-gradient(180deg,var(--magenta),var(--purple));padding:18px}
.hero-inner{position:relative;width:100%;height:100%;background:var(--white);border-radius:46px}
.hero-title{left:326px;top:48px;font-family:'Lobster Two',cursive;font-style:italic;font-weight:700;font-size:26px;line-height:29px;letter-spacing:1px;white-space:nowrap}
.hero-title .l1{color:#c05aa6}.hero-title .l2{color:#7b6fc9}.hero-title .l3{color:#2a7fc4}
.dots{left:640px;top:236px;display:flex;gap:5px}
.dots i{width:11px;height:11px;border-radius:50%;background:var(--cyan);display:block}
.dots i.on{background:var(--purple-deep)}

/* who are we */
.about{left:155px;top:497px;width:399px;height:228px;border-radius:10px;background:linear-gradient(180deg,var(--cyan),var(--cyan-light));box-shadow:0 3px 8px rgba(0,0,0,.2)}
.ribbon{left:143px;top:513px;width:222px;height:34px;background:linear-gradient(180deg,#1c9fd4,#0d78b6);border:2px solid var(--white);color:var(--white);font-weight:700;font-size:18px;letter-spacing:1px;padding:3px 0 0 24px;clip-path:polygon(0 0,100% 0,94% 50%,100% 100%,0 100%)}
.about-text{left:176px;top:560px;width:360px;color:var(--white);font-size:11px;font-weight:600;line-height:16px}
.about-text p{margin-bottom:14px}
.btn-outline{left:435px;top:677px;width:102px;height:29px;border:2px solid var(--purple-deep);color:var(--white);font-size:13px;font-weight:600;display:flex;align-items:center;justify-content:center}

/* franchise */
.franchise{left:617px;top:492px;width:231px;height:233px;border-radius:48px 48px 40px 56px;background:linear-gradient(180deg,var(--magenta),var(--purple))}
.franchise h3{left:0;top:18px;width:231px;text-align:center;color:var(--white);font-size:18px;font-weight:700;line-height:20px}
.franchise .more{left:132px;top:184px;color:var(--white);font-size:10.5px;font-weight:700;letter-spacing:.5px}

/* products */
.products{left:143px;top:745px;width:705px;height:235px;border-radius:48px;background:linear-gradient(180deg,var(--magenta) 0%,#b0197f 55%,var(--purple) 100%)}
.card{top:777px;width:143px;height:174px;background:var(--white);border:1px dashed #d08ab8}
.price{right:0;top:0;width:42px;height:45px;background:var(--purple);color:var(--white);text-align:center;font-weight:700;font-size:15px;line-height:18px;padding-top:4px;z-index:2}
.price small{display:block;font-size:9.5px;letter-spacing:.5px}
.card .photo{left:18px;top:60px;width:108px;height:100px;border-radius:0 0 50px 50px}
.overlay{left:0;top:0;width:100%;height:100%;background:rgba(120,120,120,.7);color:var(--white)}
.overlay p{position:absolute;left:8px;top:52px;width:124px;font-size:11px;font-weight:600;line-height:15px}
.overlay .btn{position:absolute;left:27px;top:132px;width:88px;height:28px;background:var(--purple);color:var(--white);font-size:12px;font-weight:600;display:flex;align-items:center;justify-content:center}

/* footer */
.footer{left:0;top:1034px;width:989px;height:149px;background:var(--footer);border-top:4px solid var(--footer-bar)}
.fcol{top:1055px;color:var(--white);font-size:9px;line-height:17px}
.fcol h4{font-size:9.5px;font-weight:700;letter-spacing:.4px;margin-bottom:6px}
.subscribe{left:447px;top:1073px;width:155px;height:27px;background:#8e0c57;border:1px solid #d45aa0;color:#e9a7cc;font-size:10px;padding:6px 8px}
.subscribe .mail{position:absolute;right:7px;top:7px}
.follow{left:447px;top:1116px;color:var(--white);font-size:9.5px;font-weight:700}
.follow-icons{left:447px;top:1138px;display:flex;gap:7px}
.follow-icons i{width:20px;height:20px;border-radius:50%;background:var(--white);display:block;opacity:.95}
.bottom-bar{left:0;top:1183px;width:989px;height:17px;background:var(--footer-bar);color:#0b3850;font-size:9px;padding:2px 0 0 160px}
</style>
</head>
<body>
<div class="page">

  <header class="abs header">
    <div class="abs brand-box"><i class="dot"></i><span>Cloudberry</span></div>
    <div class="placeholder" role="img" aria-label="Smiling sun mascot with children on a cloud" style="left:505px;top:8px;width:135px;height:104px;border-radius:50%;background:radial-gradient(circle at 40% 40%,#ffd84a,#a9d4f0 70%)"></div>
    <div class="abs brand-name">Cloudberry</div>
    <div class="abs brand-sub">FROZEN YOGURT</div>
    <div class="abs social-bubble">
      <i style="background:#d8452f"></i><i style="background:#6f98b9"></i><i style="background:#b32424"></i><i style="background:#6f98b9"></i>
    </div>
  </header>

  <nav class="abs nav">
    <a style="left:151px">HOME</a>
    <a class="active" style="left:219px">ABOUT US</a>
    <a style="left:343px">PRODUCTS</a>
    <a style="left:465px">FARNCHISE OPPORTUNITIES</a>
    <a style="left:729px">CONTACT US</a>
  </nav>
  <div class="abs dropdown">
    <a>HOME</a><a>ABOUT US</a><a>PRODUCTS</a><a>CONTACT US</a>
  </div>

  <section class="abs hero">
    <div class="hero-inner">
      <div class="placeholder" role="img" aria-label="Photo of the frozen yogurt shop interior with a glowing counter" style="left:33px;top:35px;width:275px;height:205px;border-radius:50%;background:linear-gradient(135deg,#3a3a52,#8fd3e6 60%,#e48ac0);border:2px dashed var(--magenta)"></div>
      <div class="abs hero-title"><div class="l1">Topping And Flavors,</div><div class="l2">Everything For The Best</div><div class="l3">Frozen Yogurt</div></div>
      <div class="placeholder" role="img" aria-label="Cups of strawberry ice cream next to the sun mascot on a cloud" style="left:323px;top:170px;width:225px;height:90px;border-radius:30px;background:linear-gradient(90deg,#f2c4d6,#cfd3da 45%,#ffe07a 70%,#bfe3f6)"></div>
      <div class="abs dots"><i></i><i class="on"></i><i></i></div>
    </div>
  </section>

  <section>
    <div class="abs about"></div>
    <div class="abs ribbon">WHO ARE WE ?</div>
    <div class="abs about-text">
      <p>Lorem Ipsum is simply dummy text of the printing and typesetting industry. Lorem Ipsum has been the industry's standard dummy text ever since the 1500s, when an unknown printer took a galley of type and scrambled it to make a type specimen book</p>
      <p>Lorem Ipsum is simply dummy text of the printing and typesetting industry.</p>
    </div>
    <div class="abs btn-outline">Read More</div>
  </section>

  <section class="abs franchise">
    <h3 class="abs">Franchise<br>Opportunity</h3>
    <div class="placeholder" role="img" aria-label="Pink ice cream cone character" style="left:14px;top:60px;width:68px;height:165px;border-radius:40px 40px 10px 10px;background:linear-gradient(180deg,#f06aa8,#e88fbd 55%,#e7b05a)"></div>
    <div class="placeholder" role="img" aria-label="Shop interior photo" style="left:98px;top:85px;width:100px;height:72px;border-radius:20px;background:linear-gradient(135deg,#6a2f7e,#c779c8 60%,#9fd8ec)"></div>
    <div class="abs more">READ MORE</div>
  </section>

  <div class="abs products"></div>
  <div class="abs card" style="left:180px">
    <div class="placeholder photo" role="img" aria-label="Bowl of frozen yogurt with strawberry and kiwi" style="background:linear-gradient(180deg,#f4efe6,#d9e7c4 60%,#e05a5a)"></div>
    <div class="abs overlay"><p>Lorem Ipsum is simply dummy text of the printing and typesetting industry.</p><div class="btn">Read More</div></div>
    <div class="abs price">49<small>CENT</small></div>
  </div>
  <div class="abs card" style="left:343px">
    <div class="placeholder photo" role="img" aria-label="Bowl of frozen yogurt with strawberry and kiwi" style="background:linear-gradient(180deg,#f4efe6,#d9e7c4 60%,#e05a5a)"></div>
    <div class="abs price">49<small>CENT</small></div>
  </div>
  <div class="abs card" style="left:506px">
    <div class="placeholder photo" role="img" aria-label="Bowl of frozen yogurt with strawberry and kiwi" style="background:linear-gradient(180deg,#f4efe6,#d9e7c4 60%,#e05a5a)"></div>
    <div class="abs price">49<small>CENT</small></div>
  </div>
  <div class="abs card" style="left:668px">
    <div class="placeholder photo" role="img" aria-label="Bowl of frozen yogurt with strawberry and kiwi" style="background:linear-gradient(180deg,#f4efe6,#d9e7c4 60%,#e05a5a)"></div>
    <div class="abs price">49<small>CENT</small></div>
  </div>

  <div class="placeholder" role="img" aria-label="Cartoon children eating ice cream on a park bench" style="left:0;top:840px;width:176px;height:195px;border-radius:60px 80px 0 0;background:linear-gradient(180deg,#f3d2a0,#e8879a 50%,#b8dd8a)"></div>
  <div class="placeholder" role="img" aria-label="Sun mascot with children on a cloud" style="left:884px;top:952px;width:102px;height:82px;border-radius:50%;background:radial-gradient(circle at 40% 40%,#ffd84a,#a9d4f0 70%)"></div>

  <footer>
    <div class="abs footer"></div>
    <div class="abs fcol" style="left:162px"><h4>PAGES</h4>Home<br>About<br>Menu<br>Franchise Opportunity<br>Visit Us</div>
    <div class="abs fcol" style="left:297px"><h4>OTHER LINKS</h4>FAQ<br>Privacy Policy<br>Terms &amp; Conditions</div>
    <div class="abs fcol" style="left:447px"><h4>JOIN OUR NEWSLETTER</h4></div>
    <div class="abs subscribe">Subscribe
      <svg class="mail" width="16" height="12" viewBox="0 0 16 12"><rect x="0.5" y="0.5" width="15" height="11" fill="#e9a7cc"/><path d="M1 1l7 6 7-6" stroke="#8e0c57" stroke-width="1.5" fill="none"/></svg>
    </div>
    <div class="abs follow">FOLLOW US</div>
    <div class="abs follow-icons"><i></i><i></i><i></i><i></i><i></i></div>
    <div class="abs fcol" style="left:672px"><h4>VISIT US</h4>
      <div style="line-height:12px">Cloudberry Frozen Yogurt<br>48, Larkspur Lane,<br>Maple Hollow, Ohio 43012</div>
      <div style="margin-top:8px;line-height:12px"><b>Email:</b><br>hello@cloudberryyogurt.com</div>
      <div style="margin-top:8px;line-height:12px"><b>Tel:</b><br>12345 67890</div>
    </div>
    <div class="abs bottom-bar">© 2014 - Cloudberryyogurt - All Rights Reserved.</div>
  </footer>

</div>
</body>
</html>
```